Business Card Design Project - KLB

I am looking for a more sophisticated card design for my company,
"The Kestrel Bureau"

We are a consultancy focused on strategy and change in Associations and professional organisations.

I am a lawyer and psychologist with a PhD and so am looking for something that communicates seriousness and credibility but also quirky creative solutions for strategic problems, which is my field of speciality.

I am looking for something that is quietly spoken, rather than loud colours ('credible' and 'creative' are the two adjectives that I think of as competing here).

I particularly like an embossed card style - heavy white card with plain white or white and black or white and grey text.

The key logo image for the company is a question mark and I am open to suggestions and ideas on design.

I have attached a file that includes a couple of styles that have caught my eye and my thoughts on them. Hopefully they communicate what I'm looking for.
Updates

Thank you for all the great suggestions and designs.

I really appreciated the effort and creative energy you put into your designs. I have now closed the project after selecting a design and advising the successful designer of the card that I am happy with.

Regards

Target Market(s)

Organisations (CEO's and Boards), Governments, Legal professionals, Membership Associations and aspiring professionals.

Industry/Entity Type

Lawyer

Requirements
Must have
• The key logo element is a question mark (?) and this needs to be incorporated.

Embossed style - cut outs or other design ideas interest me too.

The attached file has a number of sample ideas and comments on each one that I like.
Should not have
• I like crisp, modern fonts (Myriads etc...) and do not like embellished fonts or Times etc...

```html
<!DOCTYPE html>
<html lang="en">
<head>
<meta charset="utf-8">
<title>The Kestrel Bureau – Business Card</title>
<link rel="stylesheet" href="https://fonts.googleapis.com/css2?family=Source+Sans+3:wght@400;600;700&display=swap">
<style>
  :root {
    --page: #ffffff;
    --card-base: #141516;
    --card-band: #3a3d40;
    --card-band-edge: #55595d;
    --card-glow: #2a2c2e;
    --text-main: #d9dadb;
    --text-soft: #a9acaf;
    --rule: #4a4d50;
  }
  * { margin: 0; padding: 0; box-sizing: border-box; }
  html, body {
    width: 1043px; height: 1200px; overflow: hidden;
    background: var(--page);
    font-family: "Source Sans 3", "Myriad Pro", Arial, sans-serif;
  }
  .canvas { position: relative; width: 1043px; height: 1200px; }
  .card {
    position: absolute; left: 25px; width: 993px;
    overflow: hidden; background: var(--card-base);
  }
  .card--front { top: 20px; height: 560px; }
  .card--back { top: 605px; height: 575px; }
  .card-surface { position: absolute; inset: 0; width: 100%; height: 100%; }

  /* Front */
  .front-divider {
    position: absolute; left: 470px; top: 205px; width: 1px; height: 150px;
    background: linear-gradient(to bottom, transparent, var(--rule), transparent);
  }
  .front-person {
    position: absolute; right: 540px; top: 222px; text-align: right; color: var(--text-main);
  }
  .person-name {
    font-weight: 700; font-size: 30px; letter-spacing: -0.5px; line-height: 1;
  }
  .person-name .honorific { font-size: 14px; font-weight: 600; margin-right: 4px; vertical-align: 10px; }
  .person-role { font-size: 9px; font-weight: 600; letter-spacing: 1px; color: var(--text-soft); margin-top: 2px; }
  .person-web { font-size: 15px; letter-spacing: 3px; color: var(--text-soft); margin-top: 24px; }
  .front-brand {
    position: absolute; left: 500px; top: 246px;
    font-weight: 600; font-size: 44px; line-height: 1; color: var(--text-main); letter-spacing: -0.5px;
  }

  /* Back */
  .back-divider {
    position: absolute; left: 315px; top: 170px; width: 1px; height: 250px;
    background: linear-gradient(to bottom, transparent, var(--rule), transparent);
  }
  .back-brand {
    position: absolute; left: 210px; top: 295px;
    transform: translate(-50%, -50%) rotate(-90deg);
    white-space: nowrap; font-weight: 600; font-size: 40px; color: var(--text-main); letter-spacing: -0.5px;
  }
  .contact-list { position: absolute; left: 345px; top: 192px; list-style: none; }
  .contact-row {
    display: flex; align-items: center; height: 40px; width: 560px;
    border-bottom: 1px solid rgba(90, 94, 98, 0.35);
    color: var(--text-main); font-size: 17px; font-weight: 600; letter-spacing: 0.3px; text-transform: uppercase;
  }
  .contact-row:last-child { border-bottom: none; }
  .contact-key { width: 55px; display: flex; justify-content: center; font-weight: 700; font-size: 18px; }
  .contact-key svg { width: 22px; height: 22px; fill: var(--text-soft); }
  .contact-value { padding-left: 18px; }
</style>
</head>
<body>
<main class="canvas">

  <section class="card card--front" aria-label="Card front">
    <svg class="card-surface" viewBox="0 0 993 560" preserveAspectRatio="none" aria-hidden="true">
      <defs>
        <radialGradient id="front-glow" cx="0.47" cy="0.5" r="0.55">
          <stop offset="0" stop-color="var(--card-glow)"/>
          <stop offset="1" stop-color="var(--card-base)"/>
        </radialGradient>
        <linearGradient id="front-band-top" x1="0" y1="0" x2="0" y2="1">
          <stop offset="0" stop-color="#2a2c2f"/>
          <stop offset="1" stop-color="var(--card-band)"/>
        </linearGradient>
        <linearGradient id="front-band-bottom" x1="0" y1="0" x2="0" y2="1">
          <stop offset="0" stop-color="var(--card-band)"/>
          <stop offset="1" stop-color="#232527"/>
        </linearGradient>
      </defs>
      <rect width="993" height="560" fill="url(#front-glow)"/>
      <path d="M0 0 H993 V70 Q520 10 0 120 Z" fill="url(#front-band-top)"/>
      <path d="M0 120 Q520 10 993 70" fill="none" stroke="var(--card-band-edge)" stroke-width="2"/>
      <path d="M0 445 Q480 560 993 430 V560 H0 Z" fill="url(#front-band-bottom)"/>
      <path d="M0 445 Q480 560 993 430" fill="none" stroke="var(--card-band-edge)" stroke-width="2"/>
    </svg>
    <div class="front-divider"></div>
    <div class="front-person">
      <p class="person-name"><span class="honorific">DR.</span>MARA ELLISON</p>
      <p class="person-role">DIRECTOR</p>
      <p class="person-web">WWW.KESTRELBUREAU.COM</p>
    </div>
    <p class="front-brand">The Kestrel Bureau</p>
  </section>

  <section class="card card--back" aria-label="Card back">
    <svg class="card-surface" viewBox="0 0 993 575" preserveAspectRatio="none" aria-hidden="true">
      <defs>
        <radialGradient id="back-glow" cx="0.35" cy="0.5" r="0.6">
          <stop offset="0" stop-color="var(--card-glow)"/>
          <stop offset="1" stop-color="var(--card-base)"/>
        </radialGradient>
        <linearGradient id="back-band" x1="0" y1="0" x2="0" y2="1">
          <stop offset="0" stop-color="#2a2c2f"/>
          <stop offset="1" stop-color="var(--card-band)"/>
        </linearGradient>
      </defs>
      <rect width="993" height="575" fill="url(#back-glow)"/>
      <path d="M0 0 H993 V60 Q560 160 0 40 Z" fill="url(#back-band)"/>
      <path d="M0 40 Q560 160 993 60" fill="none" stroke="var(--card-band-edge)" stroke-width="2"/>
      <path d="M0 520 Q480 380 993 505 V575 H0 Z" fill="url(#back-band)"/>
      <path d="M0 520 Q480 380 993 505" fill="none" stroke="var(--card-band-edge)" stroke-width="2"/>
    </svg>
    <p class="back-brand">The Kestrel Bureau</p>
    <div class="back-divider"></div>
    <ul class="contact-list">
      <li class="contact-row"><span class="contact-key">DR.</span><span class="contact-value">Mara Ellison</span></li>
      <li class="contact-row">
        <span class="contact-key"><svg viewBox="0 0 24 24"><path d="M3 9c0-3 4-5 9-5s9 2 9 5l-1 2h-4l-1-3H9L8 11H4z M6 12h12l2 8H4z"/></svg></span>
        <span class="contact-value">+614.3071.2846</span>
      </li>
      <li class="contact-row">
        <span class="contact-key"><svg viewBox="0 0 24 24"><path d="M3 9c0-3 4-5 9-5s9 2 9 5l-1 2h-4l-1-3H9L8 11H4z M6 12h12l2 8H4z"/></svg></span>
        <span class="contact-value">+612.9480.5173</span>
      </li>
      <li class="contact-row">
        <span class="contact-key"><svg viewBox="0 0 24 24"><path d="M2 5h20v14H2z M3 6l9 7 9-7" fill="none" stroke="var(--text-soft)" stroke-width="2"/></svg></span>
        <span class="contact-value">mara@kestrelbureau.com.au</span>
      </li>
      <li class="contact-row">
        <span class="contact-key"><svg viewBox="0 0 24 24"><path d="M12 2a7 7 0 0 0-7 7c0 5 7 13 7 13s7-8 7-13a7 7 0 0 0-7-7zm0 10a3 3 0 1 1 0-6 3 3 0 0 1 0 6z"/></svg></span>
        <span class="contact-value">P.O. Box 418, Linden Vale, Sydney, Australia</span>
      </li>
    </ul>
  </section>

</main>
</body>
</html>
```